Brookmere Recovery Center Billboard (Addiction / Alcohol / Opioid )

visit www.brookmererecovery-example.com
We are an inpatient treatment center for opioid, alcohol and drug addiction. We are looking to get multiple 12'x25' billboards in our area. Our Phone number is 1-855-CALM-NOW we are located in Auburn Indiana
We pride ourselves on a comfortable medical detox and treat our patients as family.

Target Market(s)

Current Addicts, Addicts family or friends, Factory Workers and Shopvane shoppers

Industry/Entity Type

Health Care

Font styles to use
Sans Serif

Colors
0355a3
3176b5
ffffff

Requirements
Must have
• Logo and Phone number, and Brookmere Recovery
Nice to have
• Ideas?
1.) Addiction hurts more than yourself. (Pic of little girl?)
2.) Just how much are you willing to lose?
3.) Addiction does not define you, You are what you choose to become.
4.) Indiana's most comfortable Detox
5.) Detox in unmatched comfort.
6.) Background could be patient room with logo in upper right
7.) Looking to be able to read easily from road.
Should not have
• Hard to read lettering

```html
<!DOCTYPE html>
<html lang="en">
<head>
<meta charset="utf-8">
<title>Brookmere Recovery Billboard</title>
<link rel="stylesheet" href="https://fonts.googleapis.com/css2?family=Montserrat:wght@400;600;700;800;900&family=Oswald:wght@400&display=swap">
<style>
  :root {
    --navy: #0e2b6e;
    --cyan: #12bfea;
    --ink: #262626;
    --white: #ffffff;
    --room-light: #f7f7f7;
    --room-shade: #e4e4e4;
    --stage-top: #2e2e2e;
    --stage-bottom: #8a8a8a;
  }
  * { margin: 0; padding: 0; box-sizing: border-box; }
  html, body { width: 1000px; height: 1200px; overflow: hidden; }
  body {
    background: linear-gradient(135deg, var(--stage-top), var(--stage-bottom));
    font-family: "Montserrat", sans-serif;
    position: relative;
  }
  .billboard {
    position: absolute;
    left: 40px; top: 379px;
    width: 920px; height: 442px;
    overflow: hidden;
    box-shadow: 0 10px 24px rgba(0,0,0,0.45);
  }
  .billboard-art { position: absolute; inset: 0; width: 920px; height: 442px; }
  .headline {
    position: absolute; left: 38px; top: 30px;
    font-size: 16px; line-height: 1; color: var(--ink);
  }
  .headline span { position: absolute; white-space: nowrap; line-height: 1; }
  .headline .addiction { left: 0; top: 24px; font-size: 33px; font-weight: 700; }
  .headline .hurts { left: 190px; top: 0; font-size: 70px; font-weight: 900; color: var(--navy); letter-spacing: -1px; }
  .headline .more-than { left: 0; top: 72px; font-size: 43px; font-weight: 700; }
  .headline .yourself { left: 40px; top: 112px; font-size: 76px; font-weight: 900; color: var(--cyan); letter-spacing: -1.5px; }
  .brand {
    position: absolute; left: 40px; top: 220px; width: 200px;
    text-align: center;
  }
  .brand-dot {
    width: 70px; height: 70px; border-radius: 50%;
    background: var(--navy); margin: 0 auto 18px;
  }
  .brand-name {
    font-weight: 700; font-size: 22px; color: var(--navy);
    letter-spacing: 1px; line-height: 1.15; text-transform: uppercase;
  }
  .brand-url {
    position: absolute; left: 14px; top: 392px;
    font-family: "Oswald", sans-serif; font-size: 18px; color: var(--navy);
    white-space: nowrap;
  }
  .promise {
    position: absolute; left: 306px; top: 222px; width: 130px; height: 130px;
    display: flex; align-items: center; justify-content: center;
    text-align: center; color: var(--white); font-size: 13.5px; line-height: 1.25;
  }
  .promise b { font-weight: 800; }
  .phone-line {
    position: absolute; left: 380px; top: 374px; width: 530px; height: 68px;
    display: flex; align-items: center; justify-content: center; gap: 16px;
    color: var(--white); font-weight: 800; font-size: 44px; letter-spacing: -0.5px;
  }
  .phone-line svg { width: 34px; height: 34px; flex: none; }
</style>
</head>
<body>
  <section class="billboard">
    <svg class="billboard-art" viewBox="0 0 920 442" xmlns="http://www.w3.org/2000/svg">
      <defs>
        <linearGradient id="room-tone" x1="0" y1="0" x2="1" y2="1">
          <stop offset="0" stop-color="#f7f7f7"/>
          <stop offset="1" stop-color="#e4e4e4"/>
        </linearGradient>
        <linearGradient id="photo-tone" x1="0" y1="0" x2="1" y2="1">
          <stop offset="0" stop-color="#e7b53c"/>
          <stop offset="0.35" stop-color="#9ab540"/>
          <stop offset="0.7" stop-color="#b86a3a"/>
          <stop offset="1" stop-color="#e03a5c"/>
        </linearGradient>
      </defs>
      <rect class="room-backdrop" width="920" height="442" fill="url(#room-tone)" role="img" aria-label="Faded photo of a bright patient room with bed and dresser"/>
      <path class="wave-navy" fill="#0e2b6e" d="M620 0 C560 40 545 150 510 240 C470 340 380 420 240 442 L920 442 L920 0 Z"/>
      <path class="wave-cyan" fill="#12bfea" d="M700 0 C640 25 610 120 585 200 C560 290 520 350 440 392 L920 392 L920 0 Z"/>
      <path class="hero-photo" fill="url(#photo-tone)" role="img" aria-label="Photo of a smiling curly-haired little girl in a pink shirt blowing a dandelion in a sunny meadow" d="M720 0 C660 25 630 120 605 200 C580 290 540 345 470 374 L920 374 L920 0 Z"/>
      <rect class="phone-band" x="380" y="374" width="540" height="68" fill="#0e2b6e"/>
      <circle class="promise-ring" cx="371" cy="287" r="78" fill="#12bfea"/>
      <circle class="promise-disc" cx="371" cy="287" r="71" fill="#0e2b6e"/>
    </svg>

    <h1 class="headline">
      <span class="addiction">Addiction</span>
      <span class="hurts">hurts</span>
      <span class="more-than">more than</span>
      <span class="yourself">yourself</span>
    </h1>

    <div class="brand">
      <div class="brand-dot"></div>
      <div class="brand-name">Brookmere Recovery</div>
    </div>
    <div class="brand-url">BrookmereRecovery-example.com</div>

    <p class="promise"><span>comfortable<br><b>medical detox</b><br>and treat our<br><b>patients</b><br><b>as family</b></span></p>

    <div class="phone-line">
      <svg viewBox="0 0 24 24" fill="none" stroke="#ffffff" stroke-width="1.6" stroke-linecap="round" stroke-linejoin="round" aria-hidden="true">
        <path d="M5 3h3l2 5-2.5 1.5a11 11 0 0 0 7 7L16 14l5 2v3a2 2 0 0 1-2 2A16 16 0 0 1 3 5a2 2 0 0 1 2-2z"/>
        <path d="M15 3a6 6 0 0 1 6 6"/>
        <path d="M15 6.5a2.5 2.5 0 0 1 2.5 2.5"/>
      </svg>
      <span class="phone-number">1-855-CALM-NOW</span>
    </div>
  </section>
</body>
</html>
```